Business Card Design

We need a business card design for a new company based in Melbourne Australia. We are financial broker in finance industry. We provide a wide range of finance solutions to our clients including home loans, commercial loans, business facilities, car loans, equipment loans, invoice finance, etc. The company name is from director's personal name. We would like to have a new company logo that includes TK.

Industry/Entity Type

Business

Contact Information for Business Card

company name: TK & Co Finance Pty Ltd
person's name: Desmond Okafor
role: Managing Director
Mobile: 0417 638 294
fax: 03 9561 4472
Email: desmond.okafor@tkcolending.example
Address: Suite 5/418 Marlow Avenue Elmvale Vic 3174
Credit Licence No.: 718249

```html
<!DOCTYPE html>
<html lang="en">
<head>
<meta charset="utf-8">
<title>TK &amp; Co Finance – Business Cards</title>
<link rel="stylesheet" href="https://fonts.googleapis.com/css2?family=Roboto+Condensed:wght@300;400;700&display=swap">
<style>
  :root {
    --paper: #ffffff;
    --backdrop: #e9e6e1;
    --green: #7cb233;
    --charcoal: #333333;
    --grey: #6d6e71;
    --blue-light: #0bb5ea;
    --blue-deep: #0b3f98;
    --text: #3a3a3a;
    --card-w: 487px;
    --card-h: 295px;
  }
  html, body {
    margin: 0;
    padding: 0;
    width: 1200px;
    height: 712px;
    overflow: hidden;
    background: var(--backdrop);
    font-family: "Roboto Condensed", "Arial Narrow", sans-serif;
  }
  .sheet {
    position: relative;
    width: 1200px;
    height: 712px;
  }
  .card {
    position: absolute;
    width: var(--card-w);
    height: var(--card-h);
    background: var(--paper);
    overflow: hidden;
    box-shadow: 0 2px 6px rgba(0,0,0,0.18);
  }
  .theme-green { --accent: var(--green); --edge: var(--charcoal); --brand: var(--charcoal); }
  .theme-blue  { --accent: var(--blue-deep); --edge: var(--grey); --brand: var(--grey); }

  .pos-green-front { left: 50px;  top: 35px; }
  .pos-green-back  { left: 56px;  top: 375px; }
  .pos-blue-front  { left: 660px; top: 35px; }
  .pos-blue-back   { left: 666px; top: 377px; }

  .card-art {
    position: absolute;
    inset: 0;
    width: 100%;
    height: 100%;
  }
  .band-fill-green { fill: var(--green); }
  .band-fill-dark  { fill: var(--charcoal); }
  .edge-line { fill: none; stroke: var(--edge); stroke-width: 3; stroke-linejoin: miter; }
  .accent-line { fill: none; stroke: var(--accent); stroke-width: 3; stroke-linejoin: miter; }
  .rule { stroke: var(--accent); stroke-width: 1.6; }

  /* front brand */
  .brand-front {
    position: absolute;
    left: 160px;
    top: 200px;
    display: flex;
    align-items: center;
    gap: 10px;
  }
  .brand-square {
    width: 24px;
    height: 24px;
    background: var(--accent);
  }
  .theme-blue .brand-square { background: var(--blue-light); }
  .brand-name {
    font-weight: 700;
    color: var(--brand);
    font-size: 23px;
    letter-spacing: 0.1px;
    white-space: nowrap;
  }

  /* back */
  .holder {
    position: absolute;
    left: 64px;
    top: 50px;
    color: var(--text);
  }
  .holder-name {
    font-weight: 700;
    font-size: 15px;
    line-height: 18px;
    color: var(--charcoal);
  }
  .theme-blue .holder-name { color: var(--grey); }
  .holder-role {
    font-weight: 400;
    font-size: 15px;
    line-height: 18px;
  }
  .brand-back {
    position: absolute;
    left: 296px;
    top: 90px;
    display: flex;
    align-items: center;
    gap: 6px;
  }
  .brand-back .brand-square { width: 12px; height: 12px; }
  .brand-back .brand-name { font-size: 13px; }

  .contact-list {
    list-style: none;
    margin: 0;
    padding: 0;
    position: absolute;
    left: 60px;
    top: 120px;
    color: var(--charcoal);
    font-size: 15px;
    line-height: 22.5px;
  }
  .contact-list li {
    display: flex;
    align-items: center;
    gap: 5px;
    white-space: nowrap;
  }
  .contact-icon {
    width: 12px;
    height: 12px;
    flex: none;
  }
  .icon-stroke { fill: none; stroke: var(--accent); stroke-width: 1.4; }
  .icon-fill { fill: var(--accent); }
  .theme-green .icon-stroke { stroke: var(--green); }
  .theme-green .icon-fill { fill: var(--green); }

  .licence {
    position: absolute;
    left: 178px;
    top: 232px;
    font-size: 14px;
    color: var(--charcoal);
    white-space: nowrap;
  }
  .theme-blue .licence { color: var(--grey); }
</style>
</head>
<body>
<main class="sheet">

  <!-- Green front -->
  <section class="card theme-green pos-green-front" aria-label="Card front, green">
    <svg class="card-art" viewBox="0 0 540 327" preserveAspectRatio="none" aria-hidden="true">
      <polygon class="band-fill-dark" points="0,108 116,294 142,254 168,294 540,294 540,327 0,327"/>
      <polyline class="accent-line" points="0,96 116,282 142,242 168,282 540,282"/>
      <line class="rule" x1="175" y1="198" x2="445" y2="198"/>
    </svg>
    <div class="brand-front">
      <span class="brand-square"></span>
      <span class="brand-name">TK &amp; Co Finance Pty Ltd</span>
    </div>
  </section>

  <!-- Green back -->
  <section class="card theme-green pos-green-back" aria-label="Card back, green">
    <svg class="card-art" viewBox="0 0 540 327" preserveAspectRatio="none" aria-hidden="true">
      <line class="rule" x1="0" y1="100" x2="290" y2="100"/>
      <line class="rule" x1="300" y1="96" x2="492" y2="96"/>
      <polygon class="band-fill-green" points="540,108 428,298 402,258 376,298 0,298 0,327 540,327"/>
      <polyline class="edge-line" points="540,96 426,290 402,250 378,290 0,290"/>
    </svg>
    <div class="holder">
      <div class="holder-name">Desmond Okafor</div>
      <div class="holder-role">Managing Director</div>
    </div>
    <div class="brand-back">
      <span class="brand-square"></span>
      <span class="brand-name">TK &amp; Co Finance Pty Ltd</span>
    </div>
    <ul class="contact-list">
      <li><svg class="contact-icon" viewBox="0 0 12 12"><rect class="icon-stroke" x="3" y="1" width="6" height="10" rx="1"/></svg>0417 638 294</li>
      <li><svg class="contact-icon" viewBox="0 0 12 12"><rect class="icon-stroke" x="3" y="1" width="6" height="4"/><rect class="icon-fill" x="1" y="5" width="10" height="4"/><rect class="icon-stroke" x="3" y="8" width="6" height="3"/></svg>03 9561 4472</li>
      <li><svg class="contact-icon" viewBox="0 0 12 12"><rect class="icon-stroke" x="1" y="3" width="10" height="7"/><polyline class="icon-stroke" points="1,3 6,7 11,3"/></svg>desmond.okafor@tkcolending.example</li>
      <li><svg class="contact-icon" viewBox="0 0 12 12"><polygon class="icon-fill" points="6,1 11,5 1,5"/><rect class="icon-fill" x="2" y="6" width="8" height="5"/></svg>Suite 5/418 Marlow Avenue Elmvale Vic 3174</li>
    </ul>
    <div class="licence">Credit Licence No.: 718249</div>
  </section>

  <!-- Blue front -->
  <section class="card theme-blue pos-blue-front" aria-label="Card front, blue">
    <svg class="card-art" viewBox="0 0 540 327" preserveAspectRatio="none" aria-hidden="true">
      <defs>
        <linearGradient id="band-blue-front" x1="0" y1="0" x2="0" y2="1">
          <stop offset="0" stop-color="#0b3f98"/>
          <stop offset="0.7" stop-color="#0bb5ea"/>
        </linearGradient>
      </defs>
      <polygon fill="url(#band-blue-front)" points="0,104 116,294 142,254 168,294 540,294 540,327 0,327"/>
      <polyline class="edge-line" points="0,98 116,288 142,248 168,288 540,288"/>
      <line class="rule" x1="175" y1="196" x2="445" y2="196"/>
    </svg>
    <div class="brand-front">
      <span class="brand-square"></span>
      <span class="brand-name">TK &amp; Co Finance Pty Ltd</span>
    </div>
  </section>

  <!-- Blue back -->
  <section class="card theme-blue pos-blue-back" aria-label="Card back, blue">
    <svg class="card-art" viewBox="0 0 540 327" preserveAspectRatio="none" aria-hidden="true">
      <defs>
        <linearGradient id="band-blue-back" x1="1" y1="0" x2="0.7" y2="1">
          <stop offset="0" stop-color="#0b3f98"/>
          <stop offset="0.75" stop-color="#0bb5ea"/>
        </linearGradient>
      </defs>
      <line class="rule" x1="0" y1="100" x2="290" y2="100"/>
      <line class="rule" x1="300" y1="96" x2="492" y2="96"/>
      <polygon fill="url(#band-blue-back)" points="540,108 428,298 402,258 376,298 0,298 0,327 540,327"/>
      <polyline class="edge-line" points="540,96 426,290 402,250 378,290 0,290"/>
    </svg>
    <div class="holder">
      <div class="holder-name">Desmond Okafor</div>
      <div class="holder-role">Managing Director</div>
    </div>
    <div class="brand-back">
      <span class="brand-square"></span>
      <span class="brand-name">TK &amp; Co Finance Pty Ltd</span>
    </div>
    <ul class="contact-list">
      <li><svg class="contact-icon" viewBox="0 0 12 12"><rect class="icon-stroke" x="3" y="1" width="6" height="10" rx="1"/></svg>0417 638 294</li>
      <li><svg class="contact-icon" viewBox="0 0 12 12"><rect class="icon-stroke" x="3" y="1" width="6" height="4"/><rect class="icon-fill" x="1" y="5" width="10" height="4"/><rect class="icon-stroke" x="3" y="8" width="6" height="3"/></svg>03 9561 4472</li>
      <li><svg class="contact-icon" viewBox="0 0 12 12"><rect class="icon-stroke" x="1" y="3" width="10" height="7"/><polyline class="icon-stroke" points="1,3 6,7 11,3"/></svg>desmond.okafor@tkcolending.example</li>
      <li><svg class="contact-icon" viewBox="0 0 12 12"><polygon class="icon-fill" points="6,1 11,5 1,5"/><rect class="icon-fill" x="2" y="6" width="8" height="5"/></svg>Suite 5/418 Marlow Avenue Elmvale Vic 3174</li>
    </ul>
    <div class="licence">Credit Licence No.: 718249</div>
  </section>

</main>
</body>
</html>
```